New Packaging Design Project

Wine packaging redesign. Retail partner requested a redesign of a private label wine. The old label is attached. Our partner liked the Copper Wren Hollow label and wanted something similar. There will be a logo added to the top of the label

Went on vacation/holiday

```html
<!DOCTYPE html>
<html lang="en">
<head>
<meta charset="utf-8">
<title>Sunmere Ridge Red Blend Label</title>
<link rel="stylesheet" href="https://fonts.googleapis.com/css2?family=Saira+Extra+Condensed:wght@300;400;600&display=swap">
<style>
  :root {
    --backdrop: #8f8581;
    --sky: #7fc0e6;
    --sky-haze: #b9d6e8;
    --ridge: #c79a5f;
    --ridge-dark: #9c7448;
    --hill: #5fb640;
    --hill-light: #9ed66a;
    --band-top: #6f9a80;
    --band-bottom: #3f6e4a;
    --ink: #111611;
    --ink-soft: #1d2a1e;
    --varietal: #c9ef9a;
  }
  * { margin: 0; padding: 0; box-sizing: border-box; }
  html, body {
    width: 1200px;
    height: 800px;
    overflow: hidden;
    background: var(--backdrop);
  }
  .canvas {
    width: 1200px;
    height: 800px;
    display: flex;
    align-items: center;
    justify-content: center;
  }
  .label {
    position: relative;
    width: 820px;
    height: 680px;
    overflow: hidden;
    border-radius: 4px;
    box-shadow: 0 10px 30px rgba(0,0,0,0.25);
    font-family: "Saira Extra Condensed", "Arial Narrow", sans-serif;
    background: var(--band-bottom);
  }
  .label__scene {
    position: absolute;
    left: 0;
    top: 0;
    width: 820px;
    height: 520px;
    background: linear-gradient(180deg,
      var(--sky-haze) 0%,
      var(--sky) 20%,
      var(--sky) 30%,
      var(--ridge) 46%,
      var(--ridge-dark) 62%,
      var(--hill-light) 74%,
      var(--hill) 100%);
  }
  .label__band {
    position: absolute;
    left: 0;
    top: 440px;
    width: 820px;
    height: 240px;
    display: block;
  }
  .label__name {
    position: absolute;
    top: 318px;
    left: 0;
    width: 100%;
    text-align: center;
    font-weight: 600;
    font-size: 82px;
    letter-spacing: 5px;
    color: var(--ink);
    line-height: 1;
  }
  .label__details {
    position: absolute;
    top: 500px;
    left: 0;
    width: 100%;
    text-align: center;
  }
  .label__style {
    font-weight: 300;
    font-size: 38px;
    letter-spacing: 4px;
    color: var(--ink-soft);
    line-height: 1.1;
  }
  .label__varietals {
    font-weight: 400;
    font-size: 27px;
    letter-spacing: 3px;
    color: var(--varietal);
    line-height: 1.4;
    margin-top: 12px;
  }
  .label__vintage {
    font-weight: 300;
    font-size: 30px;
    letter-spacing: 4px;
    color: var(--ink-soft);
    margin-top: 6px;
  }
</style>
</head>
<body>
  <main class="canvas">
    <section class="label">
      <div class="label__scene" role="img" aria-label="Painted landscape of blue sky, a tan mountain peak and rolling green vineyard hills"></div>
      <svg class="label__band" viewBox="0 0 820 240" preserveAspectRatio="none" aria-hidden="true">
        <defs>
          <linearGradient id="bandFill" x1="0" y1="0" x2="0" y2="1">
            <stop offset="0" stop-color="#6f9a80"/>
            <stop offset="1" stop-color="#3f6e4a"/>
          </linearGradient>
        </defs>
        <path d="M0 40 Q410 -10 820 40 L820 240 L0 240 Z" fill="url(#bandFill)"/>
      </svg>
      <h1 class="label__name">SUNMERE RIDGE</h1>
      <div class="label__details">
        <p class="label__style">RED BLEND</p>
        <p class="label__varietals">MERLOT CABERNET|SAUVIGNON<br>CABERNET|FRANS PETIT VERDOT|MALBEC</p>
        <p class="label__vintage">2020</p>
      </div>
    </section>
  </main>
</body>
</html>
```